VoRUx marketing_clinical trial operations management

create a brochure template to include the content supplied, as well as general content such as logo, contact information and etc.

```html
<!DOCTYPE html>
<html lang="en">
<head>
<meta charset="utf-8">
<title>VoRUx Brochure</title>
<link href="https://fonts.googleapis.com/css2?family=Source+Sans+3:wght@400;600;700&display=swap" rel="stylesheet">
<style>
  :root {
    --page: #ffffff;
    --panel: #2b3a48;
    --panel-deep: #1f2c38;
    --rule: #3f9ccf;
    --accent: #5ab4e4;
    --link: #39a3de;
    --text: #f2f5f8;
    --bullet: #a9dcf2;
  }
  * { margin: 0; padding: 0; box-sizing: border-box; }
  html, body {
    width: 1200px; height: 1000px; overflow: hidden;
    background: var(--page);
    font-family: "Source Sans 3", "Helvetica Neue", Arial, sans-serif;
    color: var(--text);
  }
  .brochure {
    position: absolute; left: 23px; top: 73px;
    width: 1147px; height: 811px;
    background: var(--panel);
    box-shadow: 2px 3px 8px rgba(0,0,0,0.45);
    overflow: hidden;
  }
  .intro-panel { position: absolute; left: 0; top: 0; width: 575px; height: 811px; }
  .intro-title {
    position: absolute; left: 32px; top: 16px;
    font-size: 19px; font-weight: 700; letter-spacing: 0.1px;
  }
  .title-rule {
    position: absolute; left: 0; top: 39px; width: 575px; height: 1px;
    background: var(--rule);
  }
  .copy { position: absolute; left: 35px; width: 530px; font-size: 13px; line-height: 16px; }
  .copy strong { font-weight: 700; }
  .list { position: absolute; list-style: none; width: 480px; font-size: 13px; line-height: 16px; }
  .list li { position: relative; padding-left: 17px; }
  .list li::before {
    content: ""; position: absolute; left: 0; top: 4px;
    width: 7px; height: 7px; background: var(--bullet);
  }
  .services { left: 65px; top: 114px; }
  .services li:nth-child(2) { margin-top: 21px; }
  .services li:nth-child(3) { margin-top: 21px; }
  .strengths { left: 68px; top: 322px; }
  .strengths li:nth-child(2) { margin-top: 15px; }
  .strengths li:nth-child(3) { margin-top: 15px; }
  .strengths li:nth-child(4) { margin-top: 19px; }
  .footer-rule {
    position: absolute; left: 0; top: 742px; width: 575px; height: 1px;
    background: var(--rule);
  }
  .footer-name {
    position: absolute; left: 46px; top: 757px;
    font-size: 20px; font-weight: 600; color: var(--accent);
  }
  .contact {
    position: absolute; left: 140px; top: 754px; width: 420px;
    text-align: center; font-size: 12.5px; line-height: 22px;
  }
  .cover-panel { position: absolute; left: 575px; top: 0; width: 572px; height: 811px; }
  .lab-collage {
    position: absolute; inset: 0;
    background:
      radial-gradient(ellipse at 30% 20%, rgba(120,140,160,0.35), transparent 60%),
      radial-gradient(ellipse at 80% 80%, rgba(110,130,150,0.3), transparent 55%),
      linear-gradient(160deg, #3c4c5c 0%, #2a3947 55%, #1f2c38 100%);
  }
  .cover-headline {
    position: absolute; left: 0; top: 480px; width: 572px; text-align: center;
    font-size: 26px; font-weight: 400; color: #ffffff;
  }
  .cover-name {
    position: absolute; left: 0; top: 572px; width: 572px; text-align: center;
    font-size: 46px; font-weight: 600; color: var(--accent);
  }
  .cover-web {
    position: absolute; left: 0; top: 661px; width: 572px; text-align: center;
    font-size: 21px; color: var(--link);
  }
</style>
</head>
<body>
  <div class="brochure">
    <section class="intro-panel">
      <h1 class="intro-title">VoRUx Introduction</h1>
      <div class="title-rule"></div>

      <p class="copy" style="top:64px;"><strong>VoRUx</strong> is a data-driven solution provider serving clinical development organizations around the world in the following areas:</p>

      <ul class="list services">
        <li><strong>Select best investigator sites</strong>: proven to deliver superior enrollment results</li>
        <li><strong>Assess clinical trial feasibility</strong>: reliably identify the potential challenges for clinical trials in planning, and allow our clients to proactively take action to mitigate risk</li>
        <li><strong>Process improvement support</strong>:&nbsp; quantify opportunities potentially can be improved, recommend actions to realize the opportunities, measure the impact from implementation, and reward the people who contributed to the achievement</li>
      </ul>

      <p class="copy" style="top:282px;"><strong>VoRUx</strong> differentiate itself from competitors with the following:</p>

      <ul class="list strengths">
        <li>A second to none database both in scale and in capturing the details and dynamic in clinical development around the world</li>
        <li>A method with conceptual innovation and protected by patents and know-hows</li>
        <li>Consistently superior and quantifiable results from VoRUx services</li>
        <li>Continuing input from clients including the most prominent industry leaders</li>
      </ul>

      <p class="copy" style="top:496px; width:540px;"><strong>VoRUx</strong> clients include <strong><em>Corvane</em></strong>, <strong><em>Halden</em></strong>, <strong><em>Medrix</em></strong>, <strong><em>Treloma</em></strong>, <strong><em>Ashby &amp; Crane</em></strong>, <strong><em>Neuvia Labs</em></strong>, <strong><em>Kiyora</em></strong>, and many medium and smaller sized pharmaceutical/biopharmaceutical companies.</p>

      <div class="footer-rule"></div>
      <div class="footer-name">VoRUx</div>
      <address class="contact" style="font-style:normal;">
        PO Box 42, Maple Ridge, CT 06010, United States<br>
        Email: info@vorux.com &nbsp;|&nbsp; Phone: 555-010-2233 &nbsp;|&nbsp; Fax: 555-010-4455
      </address>
    </section>

    <section class="cover-panel">
      <div class="lab-collage" role="img" aria-label="Blue-toned grid of laboratory and clinical research photographs: microscopes, glassware, DNA strands, researchers at work and data charts"></div>
      <h2 class="cover-headline">VoRUx Solution to Your Challenges</h2>
      <div class="cover-name">VoRUx</div>
      <div class="cover-web">www.vorux.com</div>
    </section>
  </div>
</body>
</html>
```